International gaming entertainment company is looking for an innovative Power Point design *

We are looking for a Power Point design for potential international investors, partners and customers in the gaming industry, meaning that a reference to internationality and gaming should become apparent.
The template should be in a reduced and clear style with a combination of innovation and tradition. It should be adaptive and suitable for various applications (tables, shapes and diagrams).
The color scheme of our company are various shades of gray and burgundy (wine-red), however as for the design in question, we are open to other meaningful suggestions (no garish colors).
Updates

Noch kein Design dabei, dass uns 100%ig überzeugt

Target Market(s)

International investors and partners in the gaming industry

Font styles to use
Serif
Sans Serif
Other font styles liked:
• Interstate

Requirements
Must have
• Clear lines
Modern
Footer line with room for classification (eg Confidential, Public) and page number

```html
<!DOCTYPE html>
<html lang="en">
<head>
<meta charset="utf-8">
<title>Deck Overview</title>
<link href="https://fonts.googleapis.com/css2?family=Raleway:wght@300;400;700;800&display=swap" rel="stylesheet">
<style>
  :root{
    --stage:#6b6b6b;
    --wine:#d40e33;
    --mist:#d9d9d9;
    --paper:#ffffff;
    --stone:#b0b0b0;
    --ash:#a9a9a9;
    --ink:#2b2b2b;
    --navy:#2e3a6b;
    --label:#d4d4d4;
  }
  *{box-sizing:border-box;margin:0;padding:0}
  html,body{width:1200px;height:568px;overflow:hidden}
  body{background:var(--stage);font-family:'Raleway',sans-serif;position:relative}
  .thumb{position:absolute;width:277px;height:156px;overflow:hidden}
  .thumb.is-selected{outline:2px solid #bdbdbd}
  .slide-no{position:absolute;font-size:11px;color:var(--label)}
  .slide{position:relative;width:400px;height:225px;transform:scale(.6925);transform-origin:0 0;--bg-a:var(--mist);--bg-b:var(--paper);--bg-c:var(--mist);--foot:#6a6a6a}
  .slide.dark{--bg-a:#4a4a4a;--bg-b:#000;--bg-c:#5c5c5c;--foot:#cfcfcf}
  .slide > *{position:absolute}
  .bg{left:0;top:0;width:400px;height:225px}
  .block{background:var(--wine);color:var(--paper)}
  .title{font-weight:800;font-size:25px;line-height:27px;text-align:center}
  .band-title{font-weight:800;font-size:17px;color:var(--paper);text-align:center;width:100%}
  .sub{font-size:9px;color:var(--ink);text-align:center}
  .body{font-weight:300;font-size:11.5px;line-height:12.5px;letter-spacing:-.2px}
  .body ul{list-style:none}
  .body li{position:relative;padding-left:7px;margin-bottom:3px}
  .body li::before{content:"";position:absolute;left:0;top:4px;width:3px;height:3px;background:currentColor}
  .footer{left:8px;right:8px;bottom:3px;height:11px;border-top:.6px solid var(--foot);color:var(--foot);font-size:6.5px;line-height:10px;font-weight:700;letter-spacing:.6px;text-transform:uppercase;display:flex;justify-content:space-between}
  .footer.light{--foot:#ffffff}
</style>
</head>
<body>

<svg width="0" height="0" style="position:absolute">
  <symbol id="backdrop" viewBox="0 0 400 225">
    <rect width="400" height="225" fill="var(--bg-a)"/>
    <ellipse cx="245" cy="112" rx="200" ry="165" fill="var(--bg-b)"/>
    <circle cx="365" cy="80" r="73" fill="var(--bg-c)"/>
  </symbol>
</svg>

<div class="thumb is-selected" style="left:7px;top:9px">
  <div class="slide">
    <svg class="bg"><use href="#backdrop"/></svg>
    <div class="block title" style="left:123px;top:0;width:154px;height:155px;padding-top:96px">Lorem<br>Ipsum</div>
    <div style="left:123px;top:157px;width:154px;height:68px;background:var(--stone)"></div>
    <div class="sub" style="left:123px;top:158px;width:154px">dolor sit amet</div>
    <div class="footer"><span>Public</span><span>01</span></div>
  </div>
</div>
<div class="slide-no" style="left:7px;top:169px">1</div>

<div class="thumb" style="left:310px;top:9px">
  <div class="slide">
    <svg class="bg"><use href="#backdrop"/></svg>
    <div class="block title" style="left:17px;top:0;width:141px;height:145px;padding-top:88px">Lorem<br>Ipsum</div>
    <div style="left:17px;top:148px;width:141px;height:77px;background:#dedede"></div>
    <div class="sub" style="left:17px;top:150px;width:141px">dolor sit amet</div>
    <div class="footer"><span>Public</span><span>02</span></div>
  </div>
</div>
<div class="slide-no" style="left:310px;top:169px">2</div>

<div class="thumb" style="left:612px;top:9px">
  <div class="slide">
    <svg class="bg"><use href="#backdrop"/></svg>
    <svg role="img" aria-label="Photo: international city skyline lit up at night" style="left:17px;top:10px;width:366px;height:198px">
      <defs><linearGradient id="nightcity" x1="0" y1="0" x2="0" y2="1">
        <stop offset="0" stop-color="#1d3d78"/><stop offset=".45" stop-color="#264a80"/>
        <stop offset=".55" stop-color="#4a4250"/><stop offset="1" stop-color="#1b1a22"/></linearGradient></defs>
      <rect width="366" height="198" fill="url(#nightcity)"/>
    </svg>
    <div class="block title" style="left:17px;top:0;width:141px;height:145px;padding-top:88px">Lorem<br>Ipsum</div>
    <div style="left:200px;top:187px;width:183px;height:18px;background:var(--paper);font-size:9.5px;padding:3px 4px;color:var(--ink)">Nam et eros felis.</div>
    <div style="left:200px;top:205px;width:183px;height:3px;background:#000"></div>
    <div class="footer" style="left:17px;right:17px"><span>Confidential</span><span>03</span></div>
  </div>
</div>
<div class="slide-no" style="left:612px;top:169px">3</div>

<div class="thumb" style="left:915px;top:9px">
  <div class="slide">
    <svg class="bg"><use href="#backdrop"/></svg>
    <div class="block" style="left:0;top:6px;width:400px;height:34px"></div>
    <div class="band-title" style="left:0;top:13px">Lorem Ipsum</div>
    <div class="body" style="left:30px;top:45px;width:170px;height:160px;background:#e2e2e2;color:var(--navy);padding:3px 4px 0 4px">
      <ul>
        <li>Lorem ipsum dolor sit amet, consectetur adipiscing elit. Ut consequat dui nec sapien porttitor fringilla.</li>
        <li>Nam posuere fringilla nisl, eu blandit justo faucibus at. Nam commodo nec est eget egestas.</li>
        <li>Cras efficitur nunc sit amet dapibus rutrum. Duis et sollicitudin orci.</li>
      </ul>
    </div>
    <svg style="left:200px;top:40px;width:200px;height:168px" viewBox="0 5 200 168">
      <text x="88" y="13" font-size="9" font-weight="700" fill="#444" text-anchor="middle" font-family="Raleway, sans-serif">Test</text>
      <g font-size="5" fill="#888" font-family="Raleway, sans-serif" text-anchor="end">
        <text x="10" y="155">0</text><text x="10" y="135">1</text><text x="10" y="115">2</text>
        <text x="10" y="95">3</text><text x="10" y="75">4</text><text x="10" y="55">5</text><text x="10" y="35">6</text>
      </g>
      <line x1="14" y1="153" x2="195" y2="153" stroke="#bbb" stroke-width=".5"/>
      <rect x="20" y="67" width="7" height="86" fill="#e4e4e4"/><rect x="28" y="105" width="7" height="48" fill="#b8b8b8"/><rect x="36" y="113" width="7" height="40" fill="var(--wine)"/>
      <rect x="60" y="103" width="7" height="50" fill="#e4e4e4"/><rect x="68" y="65" width="7" height="88" fill="#b8b8b8"/><rect x="76" y="113" width="7" height="40" fill="var(--wine)"/>
      <rect x="100" y="83" width="7" height="70" fill="#e4e4e4"/><rect x="108" y="117" width="7" height="36" fill="#b8b8b8"/><rect x="116" y="93" width="7" height="60" fill="var(--wine)"/>
      <rect x="140" y="63" width="7" height="90" fill="#e4e4e4"/><rect x="148" y="97" width="7" height="56" fill="#b8b8b8"/><rect x="156" y="53" width="7" height="100" fill="var(--wine)"/>
      <g font-size="4.5" fill="#888" font-family="Raleway, sans-serif" text-anchor="middle">
        <text x="32" y="161">Category 1</text><text x="72" y="161">Category 2</text>
        <text x="112" y="161">Category 3</text><text x="152" y="161">Category 4</text>
        <text x="92" y="168">Series 1 · Series 2 · Series 3</text>
      </g>
    </svg>
    <div class="footer"><span>Confidential</span><span>04</span></div>
  </div>
</div>
<div class="slide-no" style="left:915px;top:169px">4</div>

<div class="thumb" style="left:7px;top:201px">
  <div class="slide">
    <svg class="bg"><use href="#backdrop"/></svg>
    <div class="body" style="left:8px;top:3px;width:128px;height:163px;background:#e4e4e4;color:var(--navy);padding:2px 4px">
      <ul>
        <li>Mauris vehicula rutrum efficitur. Suspendisse laoreet augue at ornare posuere.</li>
        <li>Phasellus nec rutrum sem. Duis a orci nisl. Mauris et</li>
        <li>Aliquam convallis eleifend elementum.</li>
      </ul>
    </div>
    <div class="body" style="left:143px;top:3px;width:253px;height:163px;background:#bdbdbd;color:var(--navy);padding:2px 4px;text-align:justify">
      <ul><li>In ipsum purus, luctus ac dolor et, tincidunt sollicitudin ex. Mauris sodales tincidunt elementum. Mauris egestas sem eget eros sodales, in porta dolor consectetur. Donec iaculis ornare sollicitudin. Nunc diam sapien, congue id pretium eget, aliquam id augue. Nam ultrices lacus vitae ex porttitor consectetur. Donec quis ullamcorper sem, sit amet finibus metus. Etiam vitae tortor et lectus hendrerit lobortis egestas ut diam. Mauris posuere iaculis diam ac ultrices.</li></ul>
    </div>
    <div class="block" style="left:0;top:173px;width:400px;height:30px"></div>
    <div class="band-title" style="left:0;top:178px">Lorem Ipsum</div>
    <div class="footer"><span>Internal</span><span>05</span></div>
  </div>
</div>
<div class="slide-no" style="left:7px;top:361px">5</div>

<div class="thumb" style="left:310px;top:201px">
  <div class="slide">
    <div class="block" style="left:0;top:0;width:200px;height:225px"></div>
    <div class="band-title" style="left:0;top:100px;width:200px">Pictures 1</div>
    <svg role="img" aria-label="Photo: retro video game console with cartridges and joysticks on a table" style="left:200px;top:0;width:200px;height:225px">
      <defs><radialGradient id="console" cx=".55" cy=".6" r=".8">
        <stop offset="0" stop-color="#6a4a3a"/><stop offset=".6" stop-color="#3a2a24"/><stop offset="1" stop-color="#1e1715"/></radialGradient></defs>
      <rect width="200" height="225" fill="url(#console)"/>
    </svg>
    <div class="footer light"><span>Public</span><span>06</span></div>
  </div>
</div>
<div class="slide-no" style="left:310px;top:361px">6</div>

<div class="thumb" style="left:612px;top:201px">
  <div class="slide">
    <div style="left:200px;top:0;width:200px;height:225px;background:var(--ash)"></div>
    <div class="band-title" style="left:200px;top:100px;width:200px">Pictures 2</div>
    <svg role="img" aria-label="Photo: stacked colourful vintage tin boxes from around the world" style="left:0;top:0;width:200px;height:225px">
      <defs><linearGradient id="tins" x1="0" y1="0" x2="1" y2="1">
        <stop offset="0" stop-color="#7d8a8a"/><stop offset=".4" stop-color="#a8583c"/><stop offset=".7" stop-color="#c7a25a"/><stop offset="1" stop-color="#5b4a3a"/></linearGradient></defs>
      <rect width="200" height="225" fill="url(#tins)"/>
    </svg>
    <div class="footer light"><span>Public</span><span>07</span></div>
  </div>
</div>
<div class="slide-no" style="left:612px;top:361px">7</div>

<div class="thumb" style="left:915px;top:201px">
  <div class="slide">
    <svg class="bg"><use href="#backdrop"/></svg>
    <div class="block" style="left:0;top:0;width:197px;height:52px"></div>
    <div class="band-title" style="left:0;top:31px;width:197px;font-size:15px">Opposing Ideas</div>
    <svg style="left:0;top:52px;width:200px;height:160px" viewBox="0 52 200 160">
      <text x="100" y="62" font-size="8" fill="#444" text-anchor="middle" font-family="Raleway, sans-serif">Sales</text>
      <path d="M100,138 L100,71 A67 67 0 1 1 42,171.5 Z" fill="#dcdcdc"/>
      <path d="M100,138 L42,171.5 A67 67 0 0 1 37,115 Z" fill="#a6a6a6"/>
      <path d="M100,138 L37,115 A67 67 0 0 1 70,78 Z" fill="var(--wine)"/>
      <path d="M100,138 L70,78 A67 67 0 0 1 100,71 Z" fill="#c4c4c4"/>
      <text x="100" y="211" font-size="4.5" fill="#999" text-anchor="middle" font-family="Raleway, sans-serif">1st Qtr · 2nd Qtr · 3rd Qtr · 4th Qtr</text>
    </svg>
    <svg style="left:200px;top:0;width:200px;height:172px" viewBox="200 0 200 172" font-family="Raleway, sans-serif" font-size="9">
      <defs><polygon id="hex" points="0,-27 23.4,-13.5 23.4,13.5 0,27 -23.4,13.5 -23.4,-13.5"/></defs>
      <use href="#hex" x="260" y="44" fill="#c20a2a"/>
      <use href="#hex" x="310" y="44" fill="#b5b5b5"/>
      <use href="#hex" x="285" y="89" fill="#a3a3a3"/>
      <use href="#hex" x="335" y="89" fill="#e2e2e2"/>
      <use href="#hex" x="260" y="134" fill="#b0b0b0"/>
      <use href="#hex" x="310" y="134" fill="var(--wine)"/>
      <text x="310" y="47" fill="#fff" text-anchor="middle">Lorem</text>
      <text x="285" y="92" fill="#fff" text-anchor="middle">Ipsum</text>
      <text x="310" y="137" fill="#fff" text-anchor="middle">Dolor</text>
      <text x="341" y="47" fill="#888">Si</text>
      <text x="232" y="92" fill="#888">Amet</text>
      <text x="341" y="137" fill="#888">Elit</text>
    </svg>
    <div class="block" style="left:203px;top:172px;width:197px;height:53px"></div>
    <div class="band-title" style="left:203px;top:174px;width:197px;font-size:15px">Ideas Opposing</div>
    <div class="footer light" style="left:211px"><span>Confidential</span><span>08</span></div>
  </div>
</div>
<div class="slide-no" style="left:915px;top:361px">8</div>

<div class="thumb" style="left:7px;top:394px">
  <div class="slide"><svg class="bg"><use href="#backdrop"/></svg>
    <div class="footer"><span>Public</span><span>09</span></div></div>
</div>
<div class="slide-no" style="left:7px;top:554px">9</div>

<div class="thumb" style="left:310px;top:394px">
  <div class="slide dark"><svg class="bg"><use href="#backdrop"/></svg>
    <div class="footer"><span>Public</span><span>10</span></div></div>
</div>
<div class="slide-no" style="left:310px;top:554px">10</div>

<div class="thumb" style="left:612px;top:394px">
  <div class="slide">
    <svg class="bg"><use href="#backdrop"/></svg>
    <svg role="img" aria-label="Photo: row of classic arcade gaming cabinets in a dim room" style="left:7px;top:5px;width:386px;height:178px">
      <defs><linearGradient id="arcade" x1="0" y1="0" x2="1" y2="0">
        <stop offset="0" stop-color="#6b5a1a"/><stop offset=".3" stop-color="#c9a521"/><stop offset=".55" stop-color="#3a2a1a"/><stop offset="1" stop-color="#1f1a16"/></linearGradient></defs>
      <rect width="386" height="178" fill="url(#arcade)"/>
    </svg>
    <div style="left:15px;top:184px;font-size:3.5px;color:#5566aa">Photo credit line and licence notice placeholder text</div>
    <div class="block" style="left:0;top:191px;width:283px;height:17px"></div>
    <div class="footer"><span>Public</span><span>11</span></div>
  </div>
</div>
<div class="slide-no" style="left:612px;top:554px">11</div>

<div class="thumb" style="left:915px;top:394px">
  <div class="slide">
    <svg class="bg"><use href="#backdrop"/></svg>
    <div class="block" style="left:0;top:92px;width:365px;height:42px"></div>
    <div class="footer"><span>Public</span><span>12</span></div>
  </div>
</div>
<div class="slide-no" style="left:915px;top:554px">12</div>

</body>
</html>
```